Everything fresh, everything new

When I take over the practice, I would like to breathe new life into the practice. I want a business card design that catches the eye and brings a breath of fresh air

```html
<!DOCTYPE html>
<html lang="de">
<head>
<meta charset="utf-8">
<title>Praxisfeld – Visitenkarte</title>
<link rel="stylesheet" href="https://fonts.googleapis.com/css2?family=Montserrat:wght@400;500;700&display=swap">
<style>
  :root {
    --page-bg: #3a3a3c;
    --card-dark: #4a4a4d;
    --card-dark-deep: #3f3f42;
    --card-white: #ffffff;
    --brand-green: #8cc63f;
    --text-light: #ffffff;
    --text-dark: #4a4a4d;
  }
  * { box-sizing: border-box; margin: 0; padding: 0; }
  html, body {
    width: 1200px; height: 1200px; overflow: hidden;
    background: var(--page-bg);
    font-family: "Montserrat", sans-serif;
  }
  .sheet {
    position: relative; width: 1200px; height: 1200px;
    display: flex; flex-direction: column; align-items: center; justify-content: center; gap: 28px;
  }
  .card {
    position: relative; width: 960px; height: 548px;
    border-radius: 40px; overflow: hidden;
    box-shadow: 0 14px 30px rgba(0,0,0,0.35);
  }
  .card-front { background: var(--card-dark); }
  .front-shapes { position: absolute; inset: 0; }
  .brand {
    position: absolute; display: flex; align-items: center; gap: 16px;
  }
  .brand-dot {
    width: 26px; height: 26px; border-radius: 50%; background: var(--brand-green);
  }
  .brand-name { font-weight: 700; letter-spacing: -0.5px; }
  .card-front .brand { left: 60px; top: 236px; }
  .card-front .brand-name { font-size: 54px; color: var(--text-dark); }

  .contact {
    position: absolute; left: 640px; top: 140px; color: var(--text-light);
  }
  .contact-name {
    font-size: 42px; font-weight: 700; color: var(--brand-green); line-height: 1;
  }
  .contact-role { font-size: 24px; font-weight: 400; margin-top: 4px; letter-spacing: 0.5px; }
  .contact-list { list-style: none; margin-top: 26px; }
  .contact-list li {
    display: flex; align-items: flex-start; gap: 14px;
    font-size: 22px; line-height: 1.3; margin-bottom: 6px;
  }
  .contact-list svg { flex: none; width: 24px; height: 24px; margin-top: 3px; fill: var(--brand-green); }

  .card-back {
    background: radial-gradient(ellipse at 55% 45%, #58585b 0%, var(--card-dark) 45%, var(--card-dark-deep) 100%);
  }
  .card-back .brand { left: 50%; top: 50%; transform: translate(-50%, -50%); gap: 22px; }
  .card-back .brand-dot { width: 38px; height: 38px; }
  .card-back .brand-name { font-size: 84px; color: var(--text-light); }
</style>
</head>
<body>
<main class="sheet">
  <section class="card card-front" aria-label="Vorderseite">
    <svg class="front-shapes" viewBox="0 0 960 548" preserveAspectRatio="none" aria-hidden="true">
      <path d="M0,0 H335 C540,60 660,270 618,548 H0 Z" fill="var(--brand-green)"/>
      <path d="M0,0 H318 C505,70 612,270 586,548 H0 Z" fill="var(--card-white)"/>
      <path d="M0,0 H300 C480,75 585,270 566,548 H0 Z" fill="var(--brand-green)"/>
      <path d="M0,0 H290 C462,80 565,270 545,548 H0 Z" fill="var(--card-white)"/>
    </svg>
    <div class="brand">
      <span class="brand-dot"></span>
      <span class="brand-name">Praxisfeld</span>
    </div>
    <div class="contact">
      <p class="contact-name">FULL NAME</p>
      <p class="contact-role">POSITION</p>
      <ul class="contact-list">
        <li>
          <svg viewBox="0 0 24 24"><path d="M6.6 10.8a15.1 15.1 0 0 0 6.6 6.6l2.2-2.2a1 1 0 0 1 1-.25 11.4 11.4 0 0 0 3.6.57 1 1 0 0 1 1 1V20a1 1 0 0 1-1 1A17 17 0 0 1 3 4a1 1 0 0 1 1-1h3.5a1 1 0 0 1 1 1c0 1.25.2 2.45.57 3.57a1 1 0 0 1-.25 1z"/></svg>
          <span>(000) 000 0000</span>
        </li>
        <li>
          <svg viewBox="0 0 24 24"><path d="M2 5h20v14H2z M3.5 6.5 12 13l8.5-6.5" fill="none" stroke="var(--brand-green)" stroke-width="2"/></svg>
          <span>email@company.com</span>
        </li>
        <li>
          <svg viewBox="0 0 24 24"><g fill="none" stroke="var(--brand-green)" stroke-width="1.8"><circle cx="12" cy="12" r="9.5"/><ellipse cx="12" cy="12" rx="4" ry="9.5"/><path d="M2.5 12h19M4 7h16M4 17h16"/></g></svg>
          <span>www.company.com</span>
        </li>
        <li>
          <svg viewBox="0 0 24 24"><path d="M12 2a7 7 0 0 0-7 7c0 5.2 7 13 7 13s7-7.8 7-13a7 7 0 0 0-7-7zm0 9.5A2.5 2.5 0 1 1 12 6.5a2.5 2.5 0 0 1 0 5z"/></svg>
          <span>123 Name Street, 000<br>Your City, 00000-000</span>
        </li>
      </ul>
    </div>
  </section>

  <section class="card card-back" aria-label="Rückseite">
    <div class="brand">
      <span class="brand-dot"></span>
      <span class="brand-name">Praxisfeld</span>
    </div>
  </section>
</main>
</body>
</html>
```